HVAC Design Services

I want a brochure to market my services. I own TOVEN Design Services LLC. I specialize in Mechanical Design with HVAC Design being my
specialty. I also do Plumbing and Civil Design. I have a strong resume with over 30 years experience. I was the Lead Mechanical Designer and Cad Manager for the mechanical group at an Architectural Engineering company for over 10 years.

I would like a professional looking brochure to pass out to engineering offices. I am targeting over-load work, when an office is so busy they need temporary help. Special project. Freeing up the engineer with my experience and capability to work with little to no direction .

1. HVAC Design
a) Calculate cfm
b) Layout and route ductwork
c) Size Ductwork
d) Choose and Layout grilles, registers and diffusers
e) Choose equipment and locate on plans
f) Create HVAC Floor Plans, Sections, Details and Schedules

2. Plumbing Design
a) Layout and route plumbing
b) Size piping
c) Create Plumbing Floor Plans, Sections, Details and Schedules.

3. VectorCAD 3D Modeling

4. Civil and GIS experience

5. VectorCAD 3D Modeling

6. Some Electrical and Structural Design experience

```html
<!DOCTYPE html>
<html lang="en">
<head>
<meta charset="utf-8">
<title>TOVEN Design Services LLC – Brochure</title>
<link rel="stylesheet" href="https://fonts.googleapis.com/css2?family=Archivo:wdth,wght@100..125,400..900&family=Montserrat:wght@400;500;600&display=swap">
<style>
  :root{
    --green:#6cb33f;
    --green-light:#84c25a;
    --dark:#313131;
    --white:#ffffff;
    --canvas:#f1f6e5;
    --muted:#dcdcdc;
  }
  *{margin:0;padding:0;box-sizing:border-box}
  html,body{width:1200px;height:830px;overflow:hidden;background:var(--canvas)}
  body{position:relative;font-family:"Montserrat",Arial,sans-serif}

  .page{position:absolute;top:74px;width:484px;height:684px;overflow:hidden;background:var(--dark)}
  .page--front{left:84px}
  .page--back{left:633px}

  .wide{font-family:"Archivo",Arial,sans-serif;font-stretch:125%;font-weight:900}

  /* FRONT */
  .front-shapes{position:absolute;inset:0}
  .photo-crew{position:absolute;left:37px;top:37px;width:171px;height:252px;
    background:linear-gradient(160deg,#d9d4c8 0%,#b9a78a 40%,#6f7a86 75%,#8a7a5f 100%)}
  .blueprint{position:absolute;left:208px;top:37px;width:276px;height:129px;
    background:linear-gradient(135deg,var(--green-light),var(--green))}
  .need{position:absolute;left:34px;top:646px;width:432px;transform-origin:top left;transform:rotate(-90deg);
    color:var(--white);font-size:118px;line-height:.82;letter-spacing:2px;white-space:nowrap;text-align:center}
  .headline{position:absolute;right:38px;top:190px;text-align:right;color:#1f1f1f;font-size:36px;line-height:37.6px}
  .headline .accent{color:var(--green)}
  .about-title{position:absolute;right:31px;top:402px;color:var(--green);font-size:19px;line-height:1}
  .about-text{position:absolute;left:140px;top:427px;width:314px;color:var(--white);
    font-family:"Archivo",Arial,sans-serif;font-stretch:100%;font-weight:400;font-size:7.9px;line-height:9.72px;
    text-align:justify;text-align-last:right}
  .side-label{position:absolute;left:0;right:0;top:651px;text-align:center;color:var(--white);
    font-family:"Archivo",Arial,sans-serif;font-stretch:125%;font-weight:700;font-size:15px;letter-spacing:4px}

  /* BACK */
  .role{position:absolute;left:43px;top:40px;color:var(--white);font-size:7.4px;font-weight:500}
  .phone{position:absolute;right:42px;top:34px;color:var(--green);font-size:15.5px;letter-spacing:.5px}
  .name-first{position:absolute;left:60px;top:110px;color:var(--white);font-size:56px;line-height:1;letter-spacing:1px}
  .name-last{position:absolute;right:60px;top:162px;color:transparent;-webkit-text-stroke:1.3px var(--white);
    font-size:56px;line-height:1;letter-spacing:1px}
  .rule{position:absolute;left:42px;width:408px;top:270px;height:1px;background:var(--green)}
  .section-title{position:absolute;color:var(--white);font-size:20px;line-height:26px}
  .section-title--services{left:45px;top:288px}
  .section-title--history{left:270px;top:287px}
  .services{position:absolute;left:45px;top:353px;list-style:none;width:160px}
  .services li{display:flex;color:var(--white);font-size:8.4px;line-height:10px;margin-bottom:9.6px}
  .services .num{font-family:"Archivo",Arial,sans-serif;font-stretch:125%;font-weight:900;width:16px;flex:none}
  .brand{position:absolute;left:43px;top:512px;width:159px;text-align:center;color:var(--white);
    font-size:13px;font-weight:600;line-height:16px;letter-spacing:.5px}
  .brand-rule{position:absolute;left:43px;top:578px;width:159px;height:1px;background:var(--green)}
  .experience{position:absolute;left:45px;top:612px;color:var(--green);font-size:17px;line-height:20px}
  .job{position:absolute;left:270px;width:180px;color:var(--muted);font-size:7.6px;line-height:9.8px}
  .job b{font-family:"Archivo",Arial,sans-serif;font-stretch:125%;font-weight:900;color:var(--white);font-size:9px;letter-spacing:.3px}
</style>
</head>
<body>

<section class="page page--front">
  <svg class="front-shapes" width="484" height="684" viewBox="0 0 484 684" aria-hidden="true">
    <path d="M0 0 H484 V166 H37 L0 118 Z" fill="var(--green)"/>
    <path d="M140 166 H484 V406 H236 Q140 406 140 300 Z" fill="var(--white)"/>
    <path d="M142 362 H208 L142 410 Z" fill="var(--green)"/>
  </svg>
  <div class="photo-crew" role="img" aria-label="Photo of three engineers in hard hats and safety vests reviewing a drawing on site"></div>
  <div class="blueprint" role="img" aria-label="Green HVAC ductwork drawing in the background"></div>
  <div class="need wide">NEED</div>
  <h1 class="headline wide">HAVAC<br>DESIGN<br><span class="accent">OR</span><br>MECHNICAL<br>DESIGN</h1>
  <h2 class="about-title wide">ABOUT ME</h2>
  <p class="about-text">I Have excellent communication skills, very friendly, Have 30 years of CAD design and 3D modeling experience. Was the CAD Lead Designer for the Mechanical Group at Halden A&amp;E with 15 years of mechanical design experience specializing in HVAC layout routing and sizing duct as well as Piping layout using VectorCAD 2014 2D/3D, DraftStation and BuildModel 2014. Experienced in design layout of mechanical (HVAC/Piping) official drawings, revision drawings, shop drawings from engineer sketches and verbal information. I maintained the mechanical standards for our group, creating and maintaining the Mechanical CAD layers, CAD blocks of details, diagrams, schedules, title blocks &amp; other components into a central repository where staff can look up and access everything needed to create and revise our mechanical drawings. All this is was done recognizing national CAD standards (NCS/MDS). Poses multi-discipline drafting skills in mechanical (HVAC/piping), Civil and a some Electrical and Structural. My experience also includes over 7 years of GIS (Geographical Information Systems) electronic mapping on the Ridgeway Site including the preparation of permit maps, road and sidewalk civil design documents, and civil site layout plans. I was part of the developing team that created RAMIS (Computer Animated Mapping Informa tion System) for the Ridgeway site I have extensive Ridgeway mapping experience creating custom maps, maintaining spatial data using RAMIS. I was responsible for preparing, importing and exporting CAD files with GIS and linking attribute data from external databases. I very familiar with the Ridgeway drawing archives, researching and obtaining drawings for various projects while at Ridgeway and at Halden A&amp;E.</p>
  <div class="side-label">FRONT SIDE</div>
</section>

<section class="page page--back">
  <p class="role">Sr. MECHANICAL/CIVIL PROJECT DESIGNER</p>
  <p class="phone wide">(555)-302-0147</p>
  <h1>
    <span class="name-first wide">DANIEL</span>
    <span class="name-last wide">MORENO</span>
  </h1>
  <div class="rule"></div>

  <h2 class="section-title section-title--services wide">SERVICES<br>I OFFER</h2>
  <ol class="services">
    <li><span class="num">1</span>HVAC Design</li>
    <li><span class="num">2</span>Plumbing Design</li>
    <li><span class="num">3</span>VectorCAD 3D Modeling</li>
    <li><span class="num">4</span>Civil and GIS experience</li>
    <li><span class="num">5</span>VectorCAD 3D Modeling</li>
    <li><span class="num">6</span>Some Electrical and Structural Design experience</li>
  </ol>

  <p class="brand">TOVEN DESIGN<br>SERVICES LLC</p>
  <div class="brand-rule"></div>
  <p class="experience wide">30 YEAR<br>EXPERIENCE</p>

  <h2 class="section-title section-title--history wide">WORK<br>HISTORY</h2>
  <p class="job" style="top:353px"><b>2019-Present KESTRA</b> -<br>Ridgeway Site (Full time Designer Specialist – All Disciplines/3D modeling) Using VectorCAD 2019, PartForge 2019 and SolidFrame 2018</p>
  <p class="job" style="top:413px"><b>2015 - 2021 NORVALTech</b> (Part Time Field Designer) 1999 - 2015 HALDEN A&amp;E (Senior Mechanical Designer &amp; CAD Lead)</p>
  <p class="job" style="top:463px"><b>1996 - 2001 Cedar Valley Tree Service</b> (Owner and Operator)</p>
  <p class="job" style="top:494px"><b>1996 - 1998 Brandt Mercer Northwest, Inc.</b> (Ridgeway Site - Mapping Services)</p>
  <p class="job" style="top:535px"><b>1994 - 1996 KMT Kessler Ridgeway Co.</b> (Ridgeway Site - Mapping Services)</p>
  <p class="job" style="top:575px"><b>1992 - 1994 Ellsworth Ridgeway Co.</b> (Ridgeway Site - Mapping Services)</p>
  <p class="job" style="top:616px"><b>1991 - 1992 DALCO, INC.</b><br>(Ridgeway Site - Mapping Services)</p>

  <div class="side-label">BACK SIDE</div>
</section>

</body>
</html>
```